Pediatric Vision Care: Myopia Control Brochure

We are a pediatric eye care practice (ophthalmology and optometry). One of our services we offer for children is myopia control, which are strategies for slowing or stopping the progression of nearsightedness. This is a service we need to sell to parents because most insurance won't pay for it. There are different options we offer that can work well for kids in different situations: glasses with Corvane lenses, atropine eye drops, and/or special contact lenses. We need a brochure we can distribute to parents to let them know about this service that would encourage them to buy it for children who need it. Attached is our initial draft brochure created by our staff that provides text that we want to keep. The images and layout can change. We probably need at least one or two photos of kids on the brochure, because this is only something that works for children who are still growing, and the target audience is parents of 4-8 year old children.

Target Market(s)

Parents of 4-8 year old children

Font styles to use
Sans Serif

Requirements
Must have
• I'm uploading our company logo that should be included somewhere on the brochure. You can include contact information (web address, phone number) for our practice that is found on our website: http://www.brookhollowkidsvision.com/
Should not have
• This should not look childish. We need the impression to be friendly but professional, medical, expert.

```html
<!DOCTYPE html>
<html lang="en">
<head>
<meta charset="utf-8">
<title>Myopia Control Brochure – Brookhollow Kids Vision</title>
<link href="https://fonts.googleapis.com/css2?family=Figtree:wght@400;500;600;700;800&display=swap" rel="stylesheet">
<style>
  :root{
    --blue:#1648c0;
    --navy:#14213d;
    --ink:#1c2230;
    --green:#6cc417;
    --green-soft:#eef8e2;
    --orange:#f7731b;
    --orange-soft:#fff0e4;
    --yellow:#f5b70c;
    --blue-soft:#e9effb;
    --page:#f3f4f6;
    --white:#ffffff;
    --rule:#d6dbe4;
  }
  *{box-sizing:border-box;margin:0;padding:0}
  html,body{width:1200px;height:675px;overflow:hidden}
  body{background:var(--page);font-family:'Figtree',sans-serif;color:var(--ink);position:relative}

  .sheet{position:absolute;top:16px;width:499px;height:643px;background:var(--white);box-shadow:0 3px 12px rgba(20,30,60,.12);overflow:hidden}
  .sheet--cover{left:75px}
  .sheet--options{left:621px}

  .brand{display:flex;align-items:center;gap:8px;position:absolute}
  .brand__dot{width:14px;height:14px;border-radius:50%;background:var(--blue)}
  .brand__name{font-weight:600;font-size:20px;line-height:1.08;color:var(--navy)}

  /* cover page */
  .hero-photo{position:absolute;left:240px;top:0;width:259px;height:420px;
    background:linear-gradient(165deg,#f2f3f2 0%,#ebe6df 30%,#dcc5b1 55%,#e6e3df 75%,#c9d3e6 100%)}
  .hero-fade{position:absolute;left:0;top:0;width:330px;height:420px;background:linear-gradient(90deg,#fff 72%,rgba(255,255,255,0))}
  .sheet--cover .brand{left:33px;top:50px}
  .cover-title{position:absolute;left:33px;top:146px;font-weight:700;font-size:57px;line-height:1;color:var(--blue);letter-spacing:-.5px}
  .cover-tagline{position:absolute;left:33px;top:269px;font-size:16px;line-height:1.45;color:var(--ink)}
  .hero-curve{position:absolute;left:0;top:320px;width:499px;height:110px}

  .info{position:absolute;top:424px;width:225px}
  .info--env{left:24px}
  .info--control{left:260px}
  .info__icon{position:absolute;left:0;top:0;width:34px;height:34px;border-radius:50%;display:flex;align-items:center;justify-content:center}
  .info--env .info__icon{border:1.5px solid var(--green)}
  .info--control .info__icon{border:1.5px solid var(--blue);background:var(--blue-soft)}
  .info__head{margin-left:44px;font-weight:600;font-size:14px;color:var(--blue);line-height:1.2}
  .info__lead{margin-left:44px;margin-top:5px;font-size:11.3px;line-height:1.4}
  .info--env .info__lead{width:150px}
  .info--control .info__lead{width:145px}
  .info__list{list-style:none;margin-top:9px}
  .info--env .info__list{margin-left:44px}
  .info--control .info__list{margin-left:12px}
  .info__list li{position:relative;padding-left:11px;font-size:10.5px;line-height:1.32;margin-bottom:4px}
  .info--control .info__list li{margin-bottom:8px}
  .info__list li::before{content:"";position:absolute;left:0;top:5px;width:4px;height:4px;border-radius:50%}
  .info--env .info__list li::before{background:var(--green)}
  .info--control .info__list li::before{background:var(--blue)}
  .info-divider{position:absolute;left:240px;top:426px;width:1px;height:150px;background:var(--rule)}

  .contact-bar{position:absolute;left:0;bottom:0;width:100%;height:49px;background:var(--blue);display:flex;align-items:center;color:var(--white);font-size:14px}
  .contact-bar__item{display:flex;align-items:center;gap:10px}
  .contact-bar__sep{width:1px;height:26px;background:rgba(255,255,255,.7);margin:0 22px}

  /* options page */
  .sheet--options .brand{left:50%;transform:translateX(-50%);top:40px}
  .options-title{position:absolute;top:112px;width:100%;text-align:center;font-weight:700;font-size:32px;color:var(--blue)}
  .options-lead{position:absolute;top:152px;width:100%;text-align:center;font-size:13.5px;line-height:1.38}

  .card{position:absolute;top:194px;width:145px;height:373px;border:1px solid;border-radius:6px;background:var(--white);overflow:hidden}
  .card--lens{left:18px;border-color:#b8c8ee}
  .card--drops{left:174px;border-color:#c9e6a8}
  .card--contacts{left:332px;border-color:#fbc49c}
  .card__head{height:60px;display:flex;align-items:center;justify-content:center;text-align:center;color:var(--white);font-weight:600;font-size:14.5px;line-height:1.25;padding-bottom:4px}
  .card--lens .card__head{background:var(--blue)}
  .card--drops .card__head{background:var(--green)}
  .card--contacts .card__head{background:var(--orange)}
  .card__photo{height:141px}
  .card--lens .card__photo{background:linear-gradient(160deg,#cfe0f2 0%,#7fa8d8 45%,#2c5aa6 100%)}
  .card--drops .card__photo{background:linear-gradient(160deg,#c9dcc0 0%,#e6ebe5 50%,#f1f2f1 100%)}
  .card--contacts .card__photo{background:linear-gradient(160deg,#dde7f2 0%,#eeeef0 55%,#f1d8c8 100%)}
  .card__badge{position:absolute;left:50%;top:49px;transform:translateX(-50%);width:34px;height:34px;border-radius:50%;background:var(--white);display:flex;align-items:center;justify-content:center;box-shadow:0 1px 3px rgba(0,0,0,.15)}
  .card__list{list-style:none;padding:13px 12px 0 9px}
  .card__list li{position:relative;padding-left:10px;font-size:10px;line-height:1.35;margin-bottom:3px}
  .card__list li::before{content:"";position:absolute;left:0;top:5px;width:4px;height:4px;border-radius:50%}
  .card--lens li::before{background:var(--blue)}
  .card--drops li::before{background:var(--green)}
  .card--contacts li::before{background:var(--orange)}
  .card__note{position:absolute;left:7px;right:6px;bottom:8px;height:52px;border-radius:5px;display:flex;align-items:center;gap:5px;padding:0 3px 0 5px;font-size:9.2px;line-height:1.35}
  .card--lens .card__note{background:var(--blue-soft)}
  .card--drops .card__note{background:var(--green-soft)}
  .card--contacts .card__note{background:var(--orange-soft)}
  .card__note svg{flex:none}

  .options-curve{position:absolute;left:0;top:575px;width:499px;height:24px}
  .options-contact{position:absolute;left:0;top:603px;width:100%;display:flex;align-items:center;justify-content:center;color:var(--blue);font-size:14.5px}
  .options-contact .contact-bar__sep{background:var(--blue);opacity:.6}
</style>
</head>
<body>

<section class="sheet sheet--cover">
  <div class="hero-photo" role="img" aria-label="Photo of a smiling girl in dark-rimmed glasses resting her chin on her hand in a bright room"></div>
  <div class="hero-fade"></div>

  <div class="brand">
    <span class="brand__dot"></span>
    <span class="brand__name">Brookhollow<br>Kids Vision</span>
  </div>

  <h1 class="cover-title">Myopia<br>Control</h1>
  <p class="cover-tagline">Protect their vision.<br>Empower their future.</p>

  <svg class="hero-curve" viewBox="0 0 499 110" preserveAspectRatio="none" aria-hidden="true">
    <defs>
      <linearGradient id="bandCover" x1="0" x2="1" y1="0" y2="0">
        <stop offset="0" stop-color="#2d63dc"/>
        <stop offset=".64" stop-color="#2d63dc"/>
        <stop offset=".65" stop-color="#6cc417"/>
        <stop offset=".8" stop-color="#6cc417"/>
        <stop offset=".81" stop-color="#f5b70c"/>
        <stop offset=".89" stop-color="#f5b70c"/>
        <stop offset=".9" stop-color="#f7731b"/>
        <stop offset="1" stop-color="#f7731b"/>
      </linearGradient>
    </defs>
    <path d="M0,20 C120,75 230,100 340,92 C410,87 460,74 499,58 L499,110 L0,110 Z" fill="#fff"/>
    <path d="M0,20 C120,75 230,100 340,92 C410,87 460,74 499,58" fill="none" stroke="url(#bandCover)" stroke-width="8"/>
  </svg>

  <div class="info info--env">
    <span class="info__icon">
      <svg width="18" height="18" viewBox="0 0 24 24" fill="none" stroke="#6cc417" stroke-width="1.8" stroke-linecap="round"><path d="M12 21V10"/><path d="M12 13c-4 0-6-3-6-6 3 0 6 2 6 6z"/><path d="M12 11c0-4 3-6 6-6 0 3-2 6-6 6z"/></svg>
    </span>
    <h2 class="info__head">Environmental options</h2>
    <p class="info__lead">Simple daily habits can help support healthy vision.</p>
    <ul class="info__list">
      <li>More time outdoors each day</li>
      <li>Regular breaks from<br>near work</li>
      <li>Good lighting for reading<br>and screen use</li>
      <li>Balanced digital device use</li>
    </ul>
  </div>

  <div class="info-divider"></div>

  <div class="info info--control">
    <span class="info__icon">
      <svg width="20" height="20" viewBox="0 0 24 24"><path d="M1.5 12C5 6 19 6 22.5 12 19 18 5 18 1.5 12z" fill="none" stroke="#1648c0" stroke-width="2"/><circle cx="12" cy="12" r="3.6" fill="#1648c0"/></svg>
    </span>
    <h2 class="info__head">Myopia control</h2>
    <p class="info__lead">Proven treatments to slow myopia progression.</p>
    <ul class="info__list">
      <li>Slows progression of nearsightedness</li>
      <li>Preserves long-term eye health</li>
      <li>Age-appropriate, safe, and effective</li>
      <li>Personalized for your child’s needs</li>
    </ul>
  </div>

  <footer class="contact-bar">
    <span class="contact-bar__item" style="margin-left:34px">
      <svg width="22" height="22" viewBox="0 0 24 24" fill="none" stroke="#fff" stroke-width="1.5"><circle cx="12" cy="12" r="10"/><ellipse cx="12" cy="12" rx="4.5" ry="10"/><path d="M2 12h20M4 7h16M4 17h16"/></svg>
      www.brookhollowkidsvision.com
    </span>
    <span class="contact-bar__sep"></span>
    <span class="contact-bar__item">
      <svg width="20" height="20" viewBox="0 0 24 24" fill="#fff"><path d="M6.6 10.8a15.1 15.1 0 0 0 6.6 6.6l2.2-2.2c.3-.3.7-.4 1-.2 1.1.4 2.3.6 3.6.6.6 0 1 .4 1 1V20c0 .6-.4 1-1 1A17 17 0 0 1 3 4c0-.6.4-1 1-1h3.5c.6 0 1 .4 1 1 0 1.3.2 2.5.6 3.6.1.3 0 .7-.2 1z"/></svg>
      (555) 218-0437
    </span>
  </footer>
</section>

<section class="sheet sheet--options">
  <div class="brand">
    <span class="brand__dot"></span>
    <span class="brand__name">Brookhollow<br>Kids Vision</span>
  </div>

  <h2 class="options-title">Treatment options</h2>
  <p class="options-lead">We offer evidence-based myopia control solutions<br>tailored to your child’s needs.</p>

  <article class="card card--lens">
    <h3 class="card__head">Lumora Corvane®<br>glasses lenses</h3>
    <span class="card__badge"><svg width="22" height="14" viewBox="0 0 28 16" fill="none" stroke="#1648c0" stroke-width="2"><circle cx="7" cy="9" r="5"/><circle cx="21" cy="9" r="5"/><path d="M12 8c1-1.5 3-1.5 4 0M2 8 1 3M26 8l1-5"/></svg></span>
    <div class="card__photo" role="img" aria-label="Close-up of a myopia control spectacle lens with a pattern of tiny lenslets"></div>
    <ul class="card__list">
      <li>Clinically proven to slow myopia progression</li>
      <li>Highly-clear vision</li>
      <li>UV protection</li>
      <li>Easy and comfortable everyday solution</li>
    </ul>
    <div class="card__note">
      <svg width="26" height="28" viewBox="0 0 24 26" fill="none" stroke="#1648c0" stroke-width="1.6" stroke-linejoin="round"><path d="M12 2 3 5.5v7c0 5.5 4 9.5 9 11.5 5-2 9-6 9-11.5v-7z"/><path d="m8 13 3 3 5-6"/></svg>
      <span>Non-invasive and effective for everyday wear</span>
    </div>
  </article>

  <article class="card card--drops">
    <h3 class="card__head">Low-dose<br>atropine</h3>
    <span class="card__badge"><svg width="14" height="18" viewBox="0 0 14 18"><path d="M7 1C5 5 2 8 2 11.5a5 5 0 0 0 10 0C12 8 9 5 7 1z" fill="#6cc417"/></svg></span>
    <div class="card__photo" role="img" aria-label="Small white dropper bottle of atropine 0.01% eye drops"></div>
    <ul class="card__list">
      <li>Clinically proven to slow myopia progression</li>
      <li>Once-daily eyedrops</li>
      <li>Well-tolerated and safe</li>
      <li>Easy to use at home</li>
    </ul>
    <div class="card__note">
      <svg width="26" height="26" viewBox="0 0 24 24" fill="none" stroke="#6cc417" stroke-width="1.6" stroke-linejoin="round"><circle cx="12" cy="12" r="11"/><path d="M10 5v5l-4 8h12l-4-8V5M9 5h6M8 15h8"/></svg>
      <span>A simple, effective pharmacological option</span>
    </div>
  </article>

  <article class="card card--contacts">
    <h3 class="card__head">Specialty<br>contact lenses</h3>
    <span class="card__badge"><svg width="20" height="14" viewBox="0 0 20 14" fill="none" stroke="#f7731b" stroke-width="1.8"><path d="M2 8c0-4 16-4 16 0-1 4-15 4-16 0z"/><path d="M3 7.5c3 1.5 11 1.5 14 0"/></svg></span>
    <div class="card__photo" role="img" aria-label="Fingertip holding a clear soft contact lens"></div>
    <ul class="card__list">
      <li>Designed to slow myopia progression</li>
      <li>Clear, comfortable vision</li>
      <li>Great for active kids</li>
      <li>Day or overnight options available</li>
    </ul>
    <div class="card__note">
      <svg width="24" height="26" viewBox="0 0 24 26" fill="none" stroke="#f7731b" stroke-width="1.6" stroke-linejoin="round"><path d="M12 2 3 5.5v7c0 5.5 4 9.5 9 11.5 5-2 9-6 9-11.5v-7z"/><path d="m8 13 3 3 5-6"/></svg>
      <span>Advanced technology for all-day or overnight wear</span>
    </div>
  </article>

  <svg class="options-curve" viewBox="0 0 499 24" preserveAspectRatio="none" aria-hidden="true">
    <defs>
      <linearGradient id="bandOptions" x1="0" x2="1" y1="0" y2="0">
        <stop offset="0" stop-color="#1648c0"/>
        <stop offset=".47" stop-color="#1648c0"/>
        <stop offset=".48" stop-color="#6cc417"/>
        <stop offset=".65" stop-color="#6cc417"/>
        <stop offset=".66" stop-color="#f5b70c"/>
        <stop offset=".8" stop-color="#f5b70c"/>
        <stop offset=".81" stop-color="#f7731b"/>
        <stop offset="1" stop-color="#f7731b"/>
      </linearGradient>
    </defs>
    <path d="M0,18 C120,6 300,6 499,4 L499,8 C300,10 120,12 0,24 Z" fill="url(#bandOptions)"/>
  </svg>

  <div class="options-contact">
    <span class="contact-bar__item">
      <svg width="22" height="22" viewBox="0 0 24 24" fill="none" stroke="#1648c0" stroke-width="1.5"><circle cx="12" cy="12" r="10"/><ellipse cx="12" cy="12" rx="4.5" ry="10"/><path d="M2 12h20M4 7h16M4 17h16"/></svg>
      www.brookhollowkidsvision.com
    </span>
    <span class="contact-bar__sep"></span>
    <span class="contact-bar__item">
      <svg width="20" height="20" viewBox="0 0 24 24" fill="#1648c0"><path d="M6.6 10.8a15.1 15.1 0 0 0 6.6 6.6l2.2-2.2c.3-.3.7-.4 1-.2 1.1.4 2.3.6 3.6.6.6 0 1 .4 1 1V20c0 .6-.4 1-1 1A17 17 0 0 1 3 4c0-.6.4-1 1-1h3.5c.6 0 1 .4 1 1 0 1.3.2 2.5.6 3.6.1.3 0 .7-.2 1z"/></svg>
      (555) 218-0437
    </span>
  </div>
</section>

</body>
</html>
```